Ferntop Contracting - Civil Construction Construction Company (Telecommunications)

Need a basic website to refine our branding to a current reflection of our service offerings. Ferntop Contracting provides civil construction services specializing in telecommunication sector.
I have started to create a website using word press. I would like to have someone refine the design and polish the overall look and functionality of the site. I would like to website to function in the wordpress format to allow for future edits and control of site.
Included site preview:
https://prv-hosts.pagebuildermock.example/7e2d90aa.com/Admin/index.html/qx_draft_preview
Coding
Coded - Design and coding required
Number of Pages Required
1 page
Look and feel
Each slider illustrates characteristics of the customer's brand and the style your logo design should communicate.

```html
<!DOCTYPE html>
<html lang="en">
<head>
<meta charset="utf-8">
<title>Ferntop Contracting</title>
<link href="https://fonts.googleapis.com/css2?family=Oswald:wght@400;500;700&family=Poppins:wght@400;500&display=swap" rel="stylesheet">
<style>
:root{
  --red:#e8202a;
  --red-dark:#c8161f;
  --black:#0b0b0b;
  --ink:#1a1a1a;
  --text:#333;
  --white:#fff;
  --dark:#23262b;
}
*{box-sizing:border-box;margin:0;padding:0}
html,body{width:1200px;height:4612px;overflow:hidden}
body{position:relative;background:var(--white);font-family:'Poppins',sans-serif;color:var(--text)}
.abs{position:absolute}
.heading{font-family:'Oswald',sans-serif;font-weight:700;text-transform:uppercase;color:var(--ink);text-align:center;letter-spacing:.5px}
.btn{position:absolute;background:var(--red);color:var(--white);font-family:'Oswald',sans-serif;font-weight:500;text-transform:uppercase;display:flex;align-items:center;justify-content:center}

.top-bar{top:0;left:0;width:1200px;height:5px;background:var(--red)}
.site-header{top:5px;left:0;width:1200px;height:85px;background:var(--white)}
.brand{position:absolute;display:flex;align-items:center;gap:10px;font-family:'Poppins',sans-serif;font-weight:500;letter-spacing:1px;text-transform:uppercase}
.brand .mark{background:var(--red)}
.site-header .brand{left:174px;top:31px;font-size:21px;color:var(--ink)}
.site-header .brand .mark{width:14px;height:14px}
.main-nav{position:absolute;right:175px;top:35px;display:flex;gap:21px;font-family:'Oswald',sans-serif;font-size:16px;text-transform:uppercase;color:#333}
.main-nav .active{color:var(--red)}

.hero{top:90px;left:0;width:1200px;height:623px;background:linear-gradient(160deg,#4b4c3d 0%,#6e6a3e 35%,#5d5a2e 60%,#3a3a2a 100%);clip-path:polygon(0 0,100% 0,100% 500px,1110px 623px,0 487px)}
.hero-title{top:254px;left:0;width:1200px;font-size:40px;line-height:45px;color:var(--white)}
.hero-btn{top:415px;left:512px;width:175px;height:51px;font-size:22px}

.section-title{font-size:46px;left:0;width:1200px}
.swoosh{position:absolute}

.profile-text{top:862px;left:180px;width:840px;font-size:18.5px;line-height:32.3px;text-align:center;color:#333}
.video{top:1050px;left:227px;width:745px;height:311px;background:linear-gradient(120deg,#3f6b2c,#8ea447 45%,#c9a52a 60%,#4c6b33)}
.play{position:absolute;left:332px;top:115px;width:80px;height:80px;border-radius:50%;border:5px solid var(--white);background:rgba(0,0,0,.25)}
.play:after{content:"";position:absolute;left:28px;top:19px;border-left:28px solid var(--white);border-top:17px solid transparent;border-bottom:17px solid transparent}
.quote{top:1390px;left:0;width:1200px;font-family:'Oswald',sans-serif;font-weight:500;font-size:18.5px;text-align:center;color:var(--ink)}
.quote.sub{top:1429px}
.service-list{top:1478px;left:298px;width:700px;display:grid;grid-template-columns:322px 1fr;row-gap:18px;font-size:14px;color:#333;list-style:none}
.service-list li{position:relative;padding-left:22px}
.service-list li:before{content:"";position:absolute;left:0;top:5px;width:11px;height:11px;background:var(--red)}
.read-more{top:1572px;left:516px;width:168px;height:59px;font-size:23px}

.why{top:1648px;left:0;width:1200px;height:725px;background:linear-gradient(180deg,#1f242b 0%,#2b2e2e 45%,#242a1c 100%);clip-path:polygon(0 130px,85px 0,1200px 135px,1200px 100%,0 100%)}
.why-title{top:1778px;color:var(--white)}
.circle{position:absolute;top:1903px;width:316px;height:316px;border-radius:50%;border:3px solid var(--white);display:flex;flex-direction:column;align-items:center}
.circle.dark{background:var(--black)}
.circle.red{background:var(--red);z-index:2}
.circle svg{margin-top:28px;flex:none}
.feature{list-style:none;margin-top:14px;font-size:14px;line-height:21px;color:var(--white);width:212px;text-align:center}
.feature li{margin-bottom:9px}
.feature li:before{content:"";display:inline-block;width:10px;height:10px;background:var(--red);margin-right:8px}
.circle.red .feature li:before{background:var(--white)}

.work-title{top:2444px}
.card{position:absolute;width:409px;height:281px;border-radius:6px;overflow:hidden;box-shadow:0 3px 10px rgba(0,0,0,.2)}
.card .photo{position:absolute;inset:0}
.card .caption{position:absolute;left:0;bottom:10px;width:340px;height:66px;background:linear-gradient(90deg,rgba(232,32,42,.95),rgba(232,32,42,.75));clip-path:polygon(0 0,100% 0,92% 100%,0 100%);font-family:'Oswald',sans-serif;font-weight:700;font-size:18.5px;line-height:22px;color:var(--white);padding:11px 0 0 22px;text-transform:uppercase}
.dots{top:3252px;left:563px;display:flex;gap:5px}
.dots span{width:10px;height:11px;background:var(--red)}

.map{top:3353px;left:0;width:1200px;height:374px;background:linear-gradient(135deg,#dfe7dc,#e9ece6 50%,#d7e3d3)}

.contact{top:3727px;left:0;width:1200px;height:571px;background:linear-gradient(180deg,#e41f28,#ea2a31)}
.contact-title{top:3808px;color:var(--white)}
.contact-text{top:3886px;left:0;width:1200px;text-align:center;font-size:17px;line-height:21px;color:var(--white)}
.field{position:absolute;background:var(--white);font-family:'Oswald',sans-serif;font-size:12.5px;color:#222;padding:18px 0 0 18px;text-transform:uppercase}
.submit{top:4143px;left:534px;width:132px;height:53px;background:var(--black);font-size:22px}

.site-footer{top:4298px;left:0;width:1200px;height:248px;background:var(--black)}
.site-footer .brand{left:0;width:1200px;justify-content:center;top:55px;font-size:42px;color:var(--white);letter-spacing:2px}
.site-footer .brand .mark{width:26px;height:26px}
.footer-nav{position:absolute;top:146px;left:0;width:1200px;display:flex;justify-content:center;font-family:'Oswald',sans-serif;font-size:17px;color:var(--white);text-transform:uppercase}
.footer-nav span{padding:0 10px;border-right:1px solid #666}
.footer-nav span:last-child{border:0}
.phone{position:absolute;top:190px;left:0;width:1200px;display:flex;justify-content:center;align-items:center;gap:10px;font-family:'Oswald',sans-serif;font-weight:500;font-size:27px;color:var(--white)}
.bottom-bar{top:4546px;left:0;width:1200px;height:66px;background:var(--red)}
.copyright{position:absolute;left:174px;top:23px;font-family:'Oswald',sans-serif;font-size:17px;color:var(--white);text-transform:uppercase}
.social{position:absolute;right:170px;top:14px;display:flex;gap:22px}
.social span{width:38px;height:38px;border-radius:50%;background:var(--white)}
</style>
</head>
<body>
<div class="abs top-bar"></div>
<header class="abs site-header">
  <div class="brand"><span class="mark"></span>Ferntop Contracting</div>
  <nav class="main-nav"><span class="active">Home</span><span>Company Profile</span><span>Why Choose Us</span><span>Our Work</span><span>Contact</span></nav>
</header>

<section class="abs hero" role="img" aria-label="Yellow trenching machine pulling an orange conduit reel across an autumn field"></section>
<h1 class="abs heading hero-title">We strive to provide creative<br>solutions,on time, on budget,<br>and beyond expectatios</h1>
<div class="btn hero-btn">Get in touch</div>

<h2 class="abs heading section-title" style="top:722px">Company Profile</h2>
<svg class="swoosh" style="left:430px;top:785px" width="340" height="40"><polygon points="0,0 340,0 316,40" fill="#e8202a"/></svg>
<p class="abs profile-text">Ferntop Contracting is a safety conscious, productive and efficient construction firm capable of all facets of civil construction. We have completed&nbsp; thousands of projects across Alberta, Saskatchewan and British Columbia working within various industry sectors. We have built a diverse team of skilled professionals who take a great deal of pride in their work and aim to achieve the highest levels of customer satisfaction.</p>
<div class="abs video" role="img" aria-label="Video still of a crew member operating a yellow trencher with a red cable reel on a lawn"><span class="play"></span></div>
<p class="abs quote">"At Ferntop Contracting we strive to provide creative solutions, on-time, on-budget and beyond expectations"</p>
<p class="abs quote sub">Ferntop Contracting is capable of providing full turnkey project execution, including:</p>
<ul class="abs service-list">
  <li>Project Design and Management</li><li>Health, Safety and Environmental Management</li>
  <li>Material Procurement and Management</li><li>Quality Assurance Management</li>
</ul>
<div class="btn read-more">Read more</div>

<section class="abs why" role="img" aria-label="Dark evening photo of heavy equipment and cable reels on a worksite"></section>
<h2 class="abs heading section-title why-title">Why Choose Us</h2>
<svg class="swoosh" style="left:448px;top:1840px" width="298" height="34"><polygon points="0,0 298,0 278,34" fill="#fff"/></svg>

<div class="circle dark" style="left:179px">
  <svg width="70" height="72" viewBox="0 0 70 72"><path d="M35 2 L66 12 V36 C66 54 52 66 35 70 C18 66 4 54 4 36 V12 Z" fill="#e8202a"/><path d="M35 2 L66 12 V36 C66 54 52 66 35 70 Z" fill="#3a3a3a"/></svg>
  <ul class="feature"><li>Accredited health and safety program</li><li>Proven track record of safety excellence</li><li>Continuous training and development of employee</li></ul>
</div>
<div class="circle red" style="left:442px">
  <svg width="76" height="76" viewBox="0 0 76 76"><g fill="#2a2a2a"><rect x="32" y="2" width="12" height="72"/><rect x="2" y="32" width="72" height="12"/><rect x="32" y="2" width="12" height="72" transform="rotate(45 38 38)"/><rect x="32" y="2" width="12" height="72" transform="rotate(-45 38 38)"/><circle cx="38" cy="38" r="26"/></g><circle cx="38" cy="38" r="12" fill="#e8202a"/><circle cx="38" cy="38" r="6" fill="#2a2a2a"/></svg>
  <ul class="feature"><li>Productive and efficient crew</li><li>Current fleet of modern equipment</li><li>Use of latest construction techniques/technologies</li></ul>
</div>
<div class="circle dark" style="left:714px">
  <svg width="130" height="72" viewBox="0 0 130 72"><rect x="6" y="10" width="30" height="26" rx="3" fill="#e8202a" transform="rotate(-35 21 23)"/><rect x="94" y="10" width="30" height="26" rx="3" fill="#e8202a" transform="rotate(35 109 23)"/><path d="M36 30 L65 22 L94 30 L78 58 L52 58 Z" fill="none" stroke="#3a3a3a" stroke-width="6" stroke-linejoin="round"/></svg>
  <ul class="feature"><li>Quality and process driven</li><li>Excellent customer service</li><li>Dependable, Reliable and Honest</li><li>Privately owned and operated</li></ul>
</div>

<h2 class="abs heading section-title work-title">Our Work</h2>
<svg class="swoosh" style="left:500px;top:2500px" width="200" height="24"><polygon points="0,0 200,0 186,24" fill="#e8202a"/></svg>

<article class="card" style="left:170px;top:2574px">
  <div class="photo" role="img" aria-label="Hydrovac truck parked on a roadside worksite" style="background:linear-gradient(180deg,#c7ccd2 0%,#9aa1a6 45%,#5f6a55 100%)"></div>
  <div class="caption">Hydrovacs utilized to safely<br>expose and identify</div>
</article>
<article class="card" style="left:620px;top:2574px">
  <div class="photo" role="img" aria-label="Blue fibre optic jetting machine with gauges" style="background:linear-gradient(135deg,#8a8f7a 0%,#4aa3c9 45%,#2b6f97 70%,#3c3c3c 100%)"></div>
  <div class="caption">Fibre optic jetting and<br>cable pulling</div>
</article>
<article class="card" style="left:170px;top:2898px">
  <div class="photo" role="img" aria-label="Red quad track plow carrying an orange HDPE reel" style="background:linear-gradient(180deg,#cfe0ef 0%,#d9452f 45%,#8c2a22 75%,#55603a 100%)"></div>
  <div class="caption">Quad track plow<br>installing 50mm HDPE</div>
</article>
<article class="card" style="left:620px;top:2898px">
  <div class="photo" role="img" aria-label="Paved park path with minimal surface disruption after drilling" style="background:linear-gradient(180deg,#b9cfd9 0%,#5e8a3f 40%,#8a9a8a 70%,#4f7a33 100%)"></div>
  <div class="caption">HDD reduces surface<br>disruption on worksites</div>
</article>
<div class="abs dots"><span></span><span></span><span></span><span></span><span></span></div>

<section class="abs map" role="img" aria-label="Street map showing the office location at 18 Larchwood Avenue, Millbrook"></section>

<section class="abs contact"></section>
<h2 class="abs heading section-title contact-title">Get in Touch</h2>
<p class="abs contact-text">If you would like to know more about our services please call or provide the<br>information below. Thank you for your interest in Ferntop Contracting</p>
<div class="field" style="left:174px;top:3962px;width:279px;height:52px">Name</div>
<div class="field" style="left:462px;top:3962px;width:279px;height:52px">Email</div>
<div class="field" style="left:750px;top:3962px;width:280px;height:52px">Phone</div>
<div class="field" style="left:174px;top:4026px;width:856px;height:138px">Please let us know how Ferntop can help</div>
<div class="btn submit">Submit</div>

<footer class="abs site-footer">
  <div class="brand"><span class="mark"></span>Ferntop Contracting</div>
  <nav class="footer-nav"><span>Home</span><span>Company Profile</span><span>Why Choose Us</span><span>Our Work</span><span>Contact</span></nav>
  <div class="phone"><svg width="26" height="26" viewBox="0 0 26 26"><circle cx="13" cy="13" r="13" fill="#fff"/><path d="M8 6 L11 6 L12 10 L10 11.5 C11 14 12 15 14.5 16 L16 14 L20 15 L20 18 C20 19 19 20 18 20 C12 20 6 14 6 8 C6 7 7 6 8 6 Z" fill="#0b0b0b"/></svg>1 (555) 014-2290</div>
</footer>
<div class="abs bottom-bar">
  <div class="copyright">Copyrights 2022 Ferntop Contracting.&nbsp;&nbsp; All rights reserved</div>
  <div class="social"><span></span><span></span><span></span></div>
</div>
</body>
</html>
```